Geschäftspapiere für Immobilien- & Steuerunternehmen
Zielgruppe
Immobilien & Steuern
Ich mache mich als Einzelunternehmer selbständig.
Ich möchte gerne ein neues Geschäftspapier mit professionellem und seriösem Erscheinungsbild.
Aufgabenstellung
Ich habe bereits ein Logo. Ebenfalls möchte ich das Logo der Morlanderbund
(Immobilientreuhänder staatlich geprüft) berücksichtigen.

```html
<!DOCTYPE html>
<html lang="de">
<head>
<meta charset="utf-8">
<title>Geschäftspapier Lukas Ambrunner</title>
<link href="https://fonts.googleapis.com/css2?family=Open+Sans:wght@400;600;700&family=Arimo:wght@400&display=swap" rel="stylesheet">
<style>
  :root {
    --orange: #f7941d;
    --black: #111111;
    --ink: #2b2b2b;
    --muted: #555555;
    --rule: #9a9a9a;
    --paper: #ffffff;
    --backdrop: #e4e5e7;
    --seal: #e2321f;
    --signature: #1b2a8c;
  }
  * { box-sizing: border-box; margin: 0; padding: 0; }
  html, body { width: 1200px; height: 945px; overflow: hidden; background: var(--backdrop); }
  body { display: flex; align-items: center; justify-content: center; font-family: "Open Sans", sans-serif; color: var(--ink); }

  .letterhead { position: relative; width: 640px; height: 905px; background: var(--paper); box-shadow: 0 6px 24px rgba(0,0,0,.18); overflow: hidden; }
  .top-band { position: absolute; top: 0; left: 0; right: 0; height: 6px; background: var(--orange); }

  .brand { position: absolute; top: 70px; left: 56px; display: flex; align-items: center; gap: 10px; }
  .brand-dot { width: 22px; height: 22px; border-radius: 50%; background: var(--orange); }
  .brand-name { font-size: 22px; font-weight: 700; color: var(--black); letter-spacing: .5px; }

  .sender-line { position: absolute; top: 148px; left: 56px; font-size: 7.5px; color: var(--ink); border-bottom: 1px solid var(--ink); padding-bottom: 1px; }
  .sender-line .sep { color: var(--orange); margin: 0 3px; }

  .contact-block { position: absolute; top: 42px; left: 420px; padding-left: 16px; border-left: 1px solid var(--ink); font-size: 9px; line-height: 1.3; }
  .contact-block h1 { font-size: 10.5px; font-weight: 700; margin: -14px 0 6px -4px; letter-spacing: .3px; }
  .contact-block ul { list-style: none; margin-bottom: 7px; }
  .contact-row { display: flex; align-items: center; gap: 5px; }
  .contact-row svg { width: 8px; height: 8px; }

  .fold-mark { position: absolute; left: 0; width: 20px; height: 1px; background: var(--rule); }

  .letter-body { position: absolute; top: 330px; left: 92px; width: 470px; font-family: "Arimo", sans-serif; font-size: 10.5px; line-height: 1.32; color: var(--ink); }
  .letter-body p { margin-bottom: 12px; }
  .salutation { margin-bottom: 12px; }

  .closing { position: absolute; top: 560px; left: 92px; font-family: "Arimo", sans-serif; font-size: 10.5px; color: var(--muted); }
  .signature { width: 200px; height: 50px; margin: 8px 0 4px 8px; background: linear-gradient(90deg, rgba(27,42,140,.18), rgba(27,42,140,.06)); border-radius: 4px; }
  .signer { margin-left: 20px; }

  .footer { position: absolute; left: 56px; right: 40px; bottom: 62px; display: flex; align-items: flex-end; gap: 14px; font-size: 9.5px; line-height: 1.35; color: var(--ink); }
  .footer-col { padding-right: 14px; }
  .footer-col + .footer-col { border-left: 1px solid var(--ink); padding-left: 14px; }
  .seal { width: 52px; height: 52px; border-radius: 50%; border: 3px solid var(--paper); outline: 1.5px solid var(--seal); background: var(--seal); margin-left: auto; align-self: flex-start; margin-top: -30px; }

  .bottom-band { position: absolute; left: 0; bottom: 0; width: 640px; height: 50px; }
</style>
</head>
<body>
  <main class="letterhead">
    <div class="top-band"></div>

    <div class="brand">
      <span class="brand-dot"></span>
      <span class="brand-name">Ambrunner</span>
    </div>
    <div class="sender-line">Mag. iur. Lukas Ambrunner<span class="sep">|</span>A-6840 Rankweil<span class="sep">|</span>Lindenweg 4</div>

    <aside class="contact-block">
      <h1>MAG. IUR. LUKAS AMBRUNNER</h1>
      <ul>
        <li>Unternehmensberater</li>
        <li>Personalverrechner</li>
        <li>Buchhalter</li>
      </ul>
      <ul>
        <li>Treuhänder für Immobilien</li>
        <li>Immobilienverwalter</li>
        <li>Immobilienmakler</li>
        <li>Bauträger</li>
      </ul>
      <div>A-6840 Rankweil, Lindenweg 4</div>
      <div class="contact-row">
        <svg viewBox="0 0 10 10"><path d="M2 1l2 2-1 1.2c.6 1.2 1.6 2.2 2.8 2.8L7 6l2 2-1.2 1.2C4.5 9 1 5.5.8 2.2z" fill="var(--orange)"/></svg>
        <span>0699 / 20 47 31 58</span>
      </div>
      <div class="contact-row">
        <svg viewBox="0 0 10 8"><rect width="10" height="8" rx="1" fill="var(--orange)"/><path d="M0 1l5 3.5L10 1" stroke="#fff" fill="none"/></svg>
        <span>ambrunner.lukas@mail.at</span>
      </div>
    </aside>

    <span class="fold-mark" style="top:300px"></span>
    <span class="fold-mark" style="top:452px"></span>
    <span class="fold-mark" style="top:640px"></span>

    <section class="letter-body">
      <div class="salutation">Sehr geehrte Damen und Herren,</div>
      <p>Sehr geehrter Herr Mustermann, Lorem ipsum dolor sit amet, consectetur adipiscing elit. Proin tincidunt, lectus id malesuada cursus, lorem augue egestas magna, ut mattis orci ante ut arcu. Sed mauris tellus, fermentum quis ligula nec, posuere pulvinar eros. Nam at mi quis velit pellentesque finibus. Donec lacus velit, faucibus mollis dolor nec, finibus pellentesque orci. Duis sed dictum elit, ut posuere arcu. Phasellus ac dolor et ante consequat rutrum nec nec tortor.</p>
      <p>Sed pretium ac enim eu viverra. Aliquam ac est eget magna convallis convallis. Aenean augue purus, finibus eget turpis quis, finibus dignissim nibh. Phasellus viverra lobortis dignissim. Duis varius turpis in sapien accumsan facilisis. Sed vehicula gravida diam a interdum. Nullam convallis ligula id erat egestas consequat. Integer consectetur ex vel aliquet iaculis. Vestibulum molestie sodales mauris, at tincidunt risus pellentesqu.</p>
    </section>

    <div class="closing">
      <div>Mit freundlichen Grüßen</div>
      <div class="signature" role="img" aria-label="Handschriftliche Unterschrift von Lukas Ambrunner in blauer Tinte"></div>
      <div class="signer">Mag. iur. Lukas Ambrunner</div>
    </div>

    <footer class="footer">
      <div class="footer-col">
        Bankdaten:<br>Talbank Alpenrhein<br>BIC: TLBKAT2BXXX<br>IBAN: ATXX XXXX XXXX XXXX XXXX
      </div>
      <div class="footer-col">
        Unternehmensdaten:<br>UID: ATU XXX XXXX<br>WKO: XXX XXX<br>REGISTER: XXX XXX
      </div>
      <div class="footer-col">
        Absolvent der<br>Sportmanagementakademie<br>der Alpenliga
      </div>
      <div class="seal" role="img" aria-label="Siegel Immobilientreuhänder staatlich geprüft"></div>
    </footer>

    <svg class="bottom-band" viewBox="0 0 640 50" preserveAspectRatio="none" aria-hidden="true">
      <polygon points="0,34 462,34 482,14 640,14 640,50 0,50" fill="var(--orange)"/>
      <polygon points="488,10 497,0 640,0 640,10" fill="var(--black)"/>
    </svg>
  </main>
</body>
</html>
```